Velmora Gems - High end custom Jewelry website

I need a web design for an online custom jewelry company called Velmora Gems. (www.velmoragems-example.com) this company specializes in high-end custom made engagement rings, wedding bands and jewelry of all kinds (necklaces, earrings, bracelets etc)All our jewelry uses diamonds so there must be a focus on diamonds on every type of jewelry we will be designing off the website.

We are a company located in New York City but our website will
aim to cater to international, national clients and as well as New York city residents.The company low overhead provides diamonds and precious metal at a discounted costs compared to its competitors. Velmora Gems makes unique custom diamond jewelry of a higher quality and at a lower price than carriage trade retail jewellers. (meaning that our company allows our customers to save money on diamond jewelry then they would if they bought from any known store or company)

The website will act as a tool for our customers to create their own jewelry. The way they will do this is by uploading pictures of what they like, they can post any pictures they want (from drawings, to actual copy and pasted pictures from other websites of designs) From these designs we will create a 3D digital image of the jewelry they like and customize it - however they want (colours, size etc) and then give them a quote in price. From the quote they will either approve it and we can have it made for them in 1 weeks time. If they decline it we will try to do whatever it is they want for the design to suit their needs.

We want the website to be simple and user friendly since people will be working on it to create their own individual jewelry pieces. Therefore some useful headings should include:

"Custom Jewellery" or something like "your design" "Custom Design"

a drop heading here should show the following steps into creating the jewelry.

step 1:
upload pictures of the designs you like
step 2:
What is your ring size?
Step 3:
What setting would you like your ring in? platinum, 14k etc..
Step 4:
What is your budget?
Step 5 :
Once you’ve uploaded pictures and give an explanation of what you want then we will contact you by phone or email and proceed to design your ring. Give us your contact info in this step.

Other then that other headings id like to see on the site are:

"Home"
main page with appealing picture which I can later add text to it explaining our company

"About us"
will include a brief section of who we are

"Wedding/engagment"

We are based in New York City and our company offers a one-to-one personal service to our clients ensuring their expectations are well met and, if we can help it, surpassed. We are a personal shopping and diamond supplier to individuals. Custom design is our speciality weather it be wedding ring, engagement ring or anniversary ring we aim to create distinctive designs that both reflect your personality as well as the beauty of the gemstones used in your piece. We use platinum, 14l-18k gold and diamonds to whatever it is that you may desire.
We in our company believe that we are privileged to be a part of one of the biggest events in our customer’s lives, and we pride ourselves on making sure that our customers have the best experience possible. As the diamond is the center piece of every engagement ring, we at VG make sure that our clients find the best diamond possible that is within their budget. Similarly, we work with established jewellery artisans from Belgium to provide the highest possible craftsmanship to a ring design of your choice. We make sure that our rings are made by the true and tried traditional methods focused on quality rather than quantity and of course our diamonds are QRB certified.

Diamonds

A section that explains where our diamonds come from. A heading will drop down here that is a diamond guide, as shown below.
Diamond Guide

An overview of the 4 C’s and different settings, a section for a brief education on diamonds.
Client Experiences

A section where clients share their experiences with Velmora Gems and can post pictures and share stories about their engagement etc.

The colour i would like to see are white and black, white and dark blue or royal blue. I don't think pastel colours will look good with this, maybe accents of purple or something pastel but for the main colours I want to keep it classic and sophisticated since it is a diamond company.

"Sign in | Check out"
where users are able to create a profile and upload their pictures and create their designs..

and a "search section"

or something along these lines or if you can incorporate both:

Exquisite craftsmanship Finest quality diamonds
Will beat any competitors price by twenty to seventy percent guaranteed
Price quotes whitin24 hours

Upload design picture or sketch
Receive price quote within 24hours
Receive and approve free customized design
Receive you jewelry in 1 week or less

Engagment Ring or necklace, earring, etc
Name
EMail
phone
Competitior Link
Budget

The final design should communicate that Velmora Gems is a custom jewelry site that allows individuals to personalize any type of jewellery they want with diamonds - at a fraction of the cost in comparison to any other out there. Our team works very hard to ensure that you will be so involved in the custom order process that there is no chance of something not being made to your requests. Jewelry is made to the highest standard or it does not ship in the first place. In the event a custom order does not suit a customer, we will take returns within 14 days of delivery less a 25% restocking fee.

Target Market(s)

middle class and upper class people ages 25-45

Industry/Entity Type

Digital

Requirements
Must have
• We have the logo now that I will attach BUT if you want to design something else please feel free ! I am open to all designs and ideas.
My logo now is simply a sketch so even if we make it look a bit more professional and classy I would like that, I think I want to keep it simple just black and white and maybe make the diamond shiny if possible. other then black in white I liked the gold and black combination too.. but as I said open to any other creative ideas!

can take pictures of jewelry off this website:
http://www.plindrowatelier-example.com/library/rings.html
Nice to have
• We already have a logo but we would like to see a banner or something that indicated saving money on diamond jewelry without it looking tacky or too cheap..

Also would like to see artistic pictures if you can of jewelry alongside very simple designs of jewelry that the masses like, (anything trendy or appealing to the eye)

cursive or elegant writing could be nice, flash could also be incorporated in the main page..

Should not have
• Nothing to old fashioned, when I mean elegant maybe just the the name of the company in cursive writing (Velmora Gems) but the actual headings and font on the website to be in a widely used font on jewelry websites. Please no hot pink colours or anything neon..
no times new roman font..

```html
<!DOCTYPE html>
<html lang="en">
<head>
<meta charset="utf-8">
<title>Velmora Gems – Custom Diamond Jewelry</title>
<link rel="stylesheet" href="https://fonts.googleapis.com/css2?family=Arimo:wght@400;700&family=Great+Vibes&display=swap">
<style>
  :root {
    --black: #000000;
    --white: #ffffff;
    --band: #2b2b2b;
    --divider: #3a3a3a;
    --frame-blue: #1a2bd0;
    --rule-blue: #3a5fb8;
    --price-yellow: #ffe600;
    --button-cyan: #4fe6f2;
    --go-blue: #8fc4ee;
    --text-font: "Arimo", Arial, sans-serif;
    --script-font: "Great Vibes", cursive;
  }
  * { margin: 0; padding: 0; box-sizing: border-box; }
  html, body { width: 997px; height: 1200px; overflow: hidden; background: var(--black); }
  body { font-family: var(--text-font); color: var(--white); position: relative; }
  .abs { position: absolute; }

  /* Header */
  .brand { left: 78px; top: 46px; font-size: 34px; font-weight: 400; letter-spacing: 3px; color: var(--white); text-transform: uppercase; }
  .quote-line { right: 50px; top: 20px; font-size: 16px; }
  .quote-line strong { font-weight: 700; margin-left: 6px; }
  .account-links { right: 53px; top: 45px; font-size: 16px; font-weight: 700; }
  .search { left: 707px; top: 78px; width: 237px; height: 22px; display: flex; }
  .search-field { flex: 1; background: var(--white); color: #666; font-size: 16px; padding: 1px 13px; line-height: 20px; }
  .search-go { width: 41px; background: linear-gradient(#b8dcf8, var(--go-blue)); color: #111; font-size: 16px; text-align: center; line-height: 22px; }

  .rule { height: 3px; background: linear-gradient(90deg, transparent, var(--rule-blue) 30%, #9ab0e0 50%, var(--rule-blue) 70%, transparent); }
  .rule-top { left: 90px; top: 125px; width: 790px; }
  .rule-hero { left: 90px; top: 556px; width: 790px; }

  .main-nav { top: 141px; left: 0; width: 997px; font-size: 16px; font-weight: 700; }
  .main-nav span { position: absolute; white-space: nowrap; }

  /* Hero */
  .hero-photo { left: 90px; top: 168px; width: 820px; height: 386px;
    background: radial-gradient(ellipse at 40% 35%, #6b4a2a 0%, #3a2716 28%, #140d08 55%, #000 80%); }
  .hero-script { left: 418px; top: 330px; font-family: var(--script-font); font-size: 66px; color: #f3f3f3; white-space: nowrap; }
  .hero-claims { left: 418px; top: 451px; font-size: 16px; font-weight: 700; line-height: 20px; }
  .newsletter-title { left: 92px; top: 465px; font-size: 16px; }
  .newsletter-field { left: 92px; top: 493px; width: 178px; height: 26px; background: #f7f7f7; border: 1px solid #bbb; color: #111; font-size: 12px; padding: 5px 8px; }
  .newsletter-submit { left: 92px; top: 528px; width: 68px; height: 16px; background: var(--button-cyan); border-radius: 3px; color: #111; font-size: 10px; text-align: center; line-height: 16px; }

  /* Company */
  .section-title { font-size: 18px; font-weight: 400; }
  .company-title { left: 90px; top: 573px; }
  .company-text { left: 92px; top: 607px; width: 288px; font-size: 16px; line-height: 23px; text-align: justify; }
  .column-divider { left: 412px; top: 570px; width: 3px; height: 302px; background: var(--divider); }

  /* Products */
  .products-title { left: 429px; top: 572px; }
  .product-photo { width: 157px; height: 98px; border: 1px solid var(--frame-blue);
    background: radial-gradient(ellipse at 50% 40%, #d6d6d6 0%, #8a8a8a 30%, #3a3a3a 60%, #181818 100%); }
  .product-name { font-size: 13px; font-weight: 700; white-space: nowrap; }
  .product-price { font-size: 15px; font-weight: 700; color: var(--price-yellow); }

  /* Design your own */
  .design-band { left: 0; top: 903px; width: 997px; height: 218px; background: var(--band); }
  .design-title { left: 12px; top: 903px; font-size: 18px; font-weight: 700; }
  .step-photo { top: 930px; width: 190px; height: 120px; }
  .step-caption { top: 1056px; font-size: 9.5px; line-height: 11px; width: 190px; }
  .process-line { left: 0; top: 1095px; width: 997px; text-align: center; font-size: 13px; word-spacing: 1px; }
  .process-line .sep { margin: 0 9px; }

  /* Footer */
  .footer-nav { top: 1158px; left: 0; width: 997px; font-size: 14px; }
  .footer-nav span { position: absolute; white-space: nowrap; }
</style>
</head>
<body>

<header>
  <div class="abs brand">Velmora Gems</div>
  <div class="abs quote-line">Call for Quote: <strong>+000 000 000 0000</strong></div>
  <div class="abs account-links">Sign in | Check out</div>
  <div class="abs search"><div class="search-field">Search</div><div class="search-go">Go</div></div>
  <div class="abs rule rule-top"></div>
  <nav class="abs main-nav">
    <span style="left:172px">&gt; Home</span>
    <span style="left:270px">&gt; About Us</span>
    <span style="left:394px">&gt; Wedding/Engagment</span>
    <span style="left:601px">&gt; Products</span>
    <span style="left:723px">&gt; Contact Us</span>
  </nav>
</header>

<section class="hero">
  <div class="abs hero-photo" role="img" aria-label="Photo of interlocking gold wedding bands set with blue and white diamonds on black"></div>
  <div class="abs hero-script">beauty and glamour</div>
  <div class="abs hero-claims">
    Exquisite craftsmanship Finest quality diamonds<br>
    Will beat any competitors price by twenty to seventy percent guaranteed<br>
    Price quotes whitin24 hours
  </div>
  <div class="abs newsletter-title">Subscribe for a newsletter</div>
  <div class="abs newsletter-field">Email address</div>
  <div class="abs newsletter-submit">Submit</div>
  <div class="abs rule rule-hero"></div>
</section>

<section class="company">
  <h2 class="abs section-title company-title">Our Company</h2>
  <p class="abs company-text">Lorem ipsum dolor sit amet, consectetur adipisicing elit, sed do eiusmod tempor incididunt ut labore et dolore magna aliqua. Ut enim ad minim veniam, quis nostrud exercitation ullamco laboris nisi ut aliquip ex ea commodo consequat. Duis aute irure dolor in reprehenderit in voluptate velit esse cillum dolore eu fugiat nulla pariatur. Excepteur sint occaecat cupidatat non proident, sunt in culpa qui officia deserunt mollit anim id est laborum.</p>
  <div class="abs column-divider"></div>
</section>

<section class="products">
  <h2 class="abs section-title products-title">Products</h2>

  <div class="abs product-photo" style="left:430px;top:603px" role="img" aria-label="Platinum diamond ring with loose diamonds"></div>
  <div class="abs product-photo" style="left:590px;top:603px" role="img" aria-label="Princess cut diamond ring with loose diamonds"></div>
  <div class="abs product-photo" style="left:748px;top:603px" role="img" aria-label="Round solitaire diamond ring with loose diamonds"></div>
  <div class="abs product-name" style="left:440px;top:707px">Exclusive Design</div>
  <div class="abs product-name" style="left:605px;top:707px">Exclusive Design</div>
  <div class="abs product-name" style="left:759px;top:707px">Exclusive Design</div>
  <div class="abs product-price" style="left:440px;top:723px">$000.00</div>
  <div class="abs product-price" style="left:606px;top:723px">$000.00</div>
  <div class="abs product-price" style="left:760px;top:723px">$000.00</div>

  <div class="abs product-photo" style="left:430px;top:746px" role="img" aria-label="Yellow diamond pendant with loose diamonds"></div>
  <div class="abs product-photo" style="left:590px;top:746px" role="img" aria-label="Woven white gold band with loose diamonds"></div>
  <div class="abs product-photo" style="left:748px;top:746px" role="img" aria-label="Rose gold solitaire ring with loose diamonds"></div>
  <div class="abs product-name" style="left:440px;top:852px">Exclusive Design</div>
  <div class="abs product-name" style="left:605px;top:852px">Exclusive Design</div>
  <div class="abs product-name" style="left:759px;top:852px">Exclusive Design</div>
  <div class="abs product-price" style="left:440px;top:870px">$000.00</div>
  <div class="abs product-price" style="left:606px;top:870px">$000.00</div>
  <div class="abs product-price" style="left:760px;top:870px">$000.00</div>
</section>

<section class="design-own">
  <div class="abs design-band"></div>
  <h2 class="abs design-title">Design Your Own Jewelry</h2>

  <div class="abs step-photo" style="left:12px;background:linear-gradient(135deg,#ffffff,#e8e8ee 60%,#d8c060)" role="img" aria-label="Pencil sketch of a ring with a blue gem"></div>
  <div class="abs step-photo" style="left:208px;background:linear-gradient(#fbfbf4,#efece0)" role="img" aria-label="Chart of ring sizes from 6 to 12.5"></div>
  <div class="abs step-photo" style="left:405px;background:radial-gradient(ellipse at 50% 50%,#e8c050,#b08a2a 60%,#e6e2d8)" role="img" aria-label="Gold nuggets"></div>
  <div class="abs step-photo" style="left:601px;background:linear-gradient(135deg,#b9c2b0,#7e8a78 50%,#c8cfc0)" role="img" aria-label="Spread of dollar banknotes"></div>
  <div class="abs step-photo" style="left:797px;background:linear-gradient(135deg,#f2f0ee,#d9d2c8 50%,#c9a85a)" role="img" aria-label="Gold and diamond wedding rings on white satin"></div>

  <p class="abs step-caption" style="left:13px">Upload pictures of the designs you like</p>
  <p class="abs step-caption" style="left:209px">What is your ring size?</p>
  <p class="abs step-caption" style="left:406px">What setting would you like your ring in?<br>platinum, 14k etc..</p>
  <p class="abs step-caption" style="left:602px">What is your budget?</p>
  <p class="abs step-caption" style="left:798px">Proceed to design your ring.<br>Give us your contact info in this step.</p>

  <p class="abs process-line">Upload design picture or sketch<span class="sep">|</span>Receive price quote within 24hours<span class="sep">|</span>Receive and approve free customized design<span class="sep">|</span>Receive your jewelry in 1 week or less</p>
</section>

<footer>
  <nav class="abs footer-nav">
    <span style="left:225px">&gt; Home</span>
    <span style="left:312px">&gt; About Us</span>
    <span style="left:419px">&gt; Wedding/Engagment</span>
    <span style="left:597px">&gt; Products</span>
    <span style="left:701px">&gt; Contact Us</span>
  </nav>
</footer>

</body>
</html>
```